Insurance Law Website

**Please note do not sell insurance, we are a law firm which specialises in Insurance law.**

We are a legal insurance firm based in Australia consisting of 150+ legal professionals.

Our initial budget for this project is around: $500

We require a design to meet the specification below, however we do want designers to come up with an interpretation of something modern but still professional, we need it to stand out above all other legal websites!

1. Responsive design
2. It should be a minimalist design, the use of background imagery is fine but we are looking to de-clutter the home page in particular and have additional content accessible through menu links to other areas such as publications, news, announcements and expert/staff pages, careers etc.
3. Something that stands out from a typical legal website.
4. The homepage should cater for a video which will contain a 'who we are' message from the CEO/Firm.
5. Colours used light/medium blues (eg: #8aabff, #bdd7fc), white
6. We also require a static information box on the page with the heading "THREE STATES, ONE FOCUS" - see image attached for full text of the box.

Visitors to our website should be aware we are an Insurance law firm, this can be achieved by using insurance focused full background imagery (no natural disasters such as floods, earthquakes etc) such as insurance buildings (Brenmoor building - London), international landmarks etc

Some websites we like certain aspects of;

http://vallemarquistone.com/ - top image boxes
http://www.pelkt.com.au/ - similar however prefer to use a FULL background image, with one full width text box at the bottom, navigation menu at the top with logo

However please don't take these examples as a sign of what the site MUST look like, please use your imagination to interpret your own vision.

Reason: Extended due to feedback provided and waiting for resubmission of designs. It appears that some people may be misunderstanding the brief, please review the brief in full before submitting any designs and let us know if you have any questions.

Reason: Apologies to those who are waiting for a decision we are reviewing and discussiing all submitted designs internally and waiting for some additional amendments to come in. We have extended the project a final time whilst we carry out our reviews. Please continue to submit any modifications and thanks again for everyone's input thus far. D+T

We have 3 days left of this project please keep submitting your designs. This is a guaranteed project.

D+T

Target Market(s)

Lawyers looking for publications, information, contact details of our lawyers and careers/job searches.

Industry/Entity Type

Insurance

Font styles to use
Sans Serif

Requirements
Must have
• Top menu to include:

Home (small icon)
Who We Are (text)
Experts (text)
Expertise (text)
Media (text)
- News (text)
- Publications (text)
Community Footprint (text)
Careers (text)
Contact (text/icon)
Search (icon - will expand on click to search in field)

Footer to include:

Copyright (text)
Privacy Policy (text)
Cookie policy (text)
Sitemap (text)
Contact (text/icon)
Profile (icon)
Print (icon)
Email (icon)

Should not have
• Stereotypical imagery such as legal scales, money bags, natural disasters etc. We are a professional firm and require designs to suit.

```html
<!DOCTYPE html>
<html lang="en">
<head>
<meta charset="utf-8">
<title>Dalton Tremayne — Insurance Law</title>
<link rel="stylesheet" href="https://fonts.googleapis.com/css2?family=Fira+Sans:ital,wght@0,400;0,500;1,400&display=swap">
<style>
  :root {
    --brand-blue: #1f4fa3;
    --call-blue: #2a63c4;
    --nav-bg: #5b5c86;
    --hero-panel: #7370a9;
    --heading-ink: #4a4a6c;
    --body-ink: #4d4c7c;
    --footer-ink: #333338;
    --band-teal: #4e9aa3;
    --frame-line: #c9c9c9;
    --white: #ffffff;
  }
  * { margin: 0; padding: 0; box-sizing: border-box; }
  html, body { width: 1200px; height: 900px; overflow: hidden; background: var(--white); }
  body { font-family: "Fira Sans", Arial, sans-serif; position: relative; }

  .page {
    position: absolute; left: 128px; top: 0; width: 950px; height: 900px;
    border-left: 1px solid var(--frame-line); border-right: 1px solid var(--frame-line);
  }

  /* Header */
  .brand {
    position: absolute; left: 17px; top: 14px;
    color: var(--brand-blue); font-weight: 400; font-size: 31px; line-height: 27px;
    display: flex; align-items: flex-start; gap: 8px;
  }
  .brand-mark { width: 10px; height: 10px; background: var(--brand-blue); opacity: .35; margin-top: 6px; }
  .call-now {
    position: absolute; left: 432px; top: 35px;
    color: var(--call-blue); font-size: 16px; font-weight: 500;
  }
  .search { position: absolute; left: 621px; top: 34px; display: flex; gap: 3px; }
  .search-field {
    width: 132px; height: 21px; border: 1px solid #9a9a9a; font: 9px Arial, sans-serif;
    color: #888; padding: 5px 6px;
  }
  .search-btn {
    height: 21px; padding: 0 7px; border: 1px solid #8a8a8a; background: linear-gradient(#f7f7f7, #dcdcdc);
    font: 9px Arial, sans-serif; line-height: 19px; color: #111;
  }
  .social { position: absolute; left: 824px; top: 29px; display: flex; gap: 7px; }
  .social span { width: 30px; height: 30px; border-radius: 50%; }
  .social .s1 { background: #55acde; }
  .social .s2 { background: #4a67b0; }
  .social .s3 { background: #2d7dc2; }

  /* Navigation */
  .main-nav {
    position: absolute; left: 0; top: 85px; width: 948px; height: 43px; background: var(--nav-bg);
  }
  .main-nav ul { list-style: none; display: flex; position: absolute; left: 93px; top: 0; height: 43px; }
  .main-nav li {
    color: var(--white); font-size: 13px; font-weight: 500; padding: 0 8px; line-height: 44px;
  }
  .main-nav li.active {
    background: var(--white); color: #111; margin-top: -13px; line-height: 70px; height: 56px; padding-top: 0;
  }
  .main-nav li.active span { display: block; padding-top: 9px; line-height: 52px; }

  /* Hero */
  .hero { position: absolute; left: 0; top: 133px; width: 948px; height: 337px; overflow: hidden; }
  .hero-photo {
    position: absolute; inset: 0;
    background: linear-gradient(200deg, #e3e6ea 0%, #a8adb4 30%, #5d636b 60%, #33373d 100%);
  }
  .hero svg { position: absolute; inset: 0; }
  .hero-copy { position: absolute; left: 14px; top: 38px; width: 420px; color: var(--white); }
  .hero-copy h1 { font-size: 21.5px; font-weight: 400; line-height: 26px; margin-bottom: 5px; white-space: nowrap; }
  .hero-copy p { font-size: 12.6px; line-height: 23.2px; }
  .read-more { font-style: italic; text-decoration: underline; font-size: 14px; margin-left: 14px; }

  /* Intro */
  .video-player { position: absolute; left: 17px; top: 493px; width: 405px; height: 249px; background: #000; }
  .video-bar {
    position: absolute; left: 0; bottom: 0; width: 100%; height: 17px; background: #1d1d1d;
    border-top: 2px solid #3a3a3a; color: #ddd; font: 7px Arial, sans-serif;
  }
  .video-time { position: absolute; left: 62px; top: 3px; }
  .intro { position: absolute; left: 445px; top: 503px; width: 480px; text-align: center; }
  .intro h2 { color: var(--heading-ink); font-size: 24.5px; font-weight: 400; letter-spacing: .5px; margin-bottom: 6px; }
  .intro p { color: var(--body-ink); font-size: 14.6px; line-height: 27.8px; }

  /* Footer */
  .footer-links {
    position: absolute; left: 0; top: 822px; width: 948px; display: flex; justify-content: center; gap: 13px;
    color: var(--footer-ink); font-size: 12.5px; font-weight: 500; padding-left: 40px;
  }
  .footer-band {
    position: absolute; left: 0; top: 857px; width: 948px; height: 43px; background: var(--band-teal);
    color: var(--white); font-size: 13px; font-weight: 500; text-align: center; line-height: 45px;
  }
</style>
</head>
<body>
<div class="page">
  <header>
    <div class="brand"><span>dalton<br>tremayne</span><span class="brand-mark"></span></div>
    <div class="call-now">Call Now- 0061-2840917</div>
    <div class="search"><div class="search-field">Find</div><div class="search-btn">Search</div></div>
    <div class="social"><span class="s1"></span><span class="s2"></span><span class="s3"></span></div>
  </header>

  <nav class="main-nav">
    <ul>
      <li>Home</li>
      <li class="active"><span>Who We Are</span></li>
      <li>Experts</li>
      <li>Expertise</li>
      <li>Media</li>
      <li>News</li>
      <li>Publications</li>
      <li>Community</li>
      <li>Footprint</li>
      <li>Careers</li>
      <li>Contact</li>
    </ul>
  </nav>

  <section class="hero">
    <div class="hero-photo" role="img" aria-label="Upward view of a modern steel insurance building with exterior lifts and pipework against a cloudy sky"></div>
    <svg width="948" height="337" viewBox="0 0 948 337">
      <polygon points="0,0 529,0 301,337 0,337" fill="#7370a9"/>
      <circle cx="918" cy="158" r="17" fill="#ffffff" fill-opacity=".25"/>
      <polyline points="913,149 922,158 913,167" fill="none" stroke="#ffffff" stroke-opacity=".7" stroke-width="3"/>
    </svg>
    <div class="hero-copy">
      <h1>Welcome to Dalton Tremayne legal insurance firm</h1>
      <p>Sample text - Far too often businesses seperate these two issues. Businesses<br>
      that create a website as a stand alone enterprise seldom get much of a<br>
      Return on Investment. You may need to update your current business<br>
      &nbsp;plan. Your online platform will create new ways to reach your<br>
      current customer base as well as help you to find new<br>
      customers. It will allow you to Measure Results, calculate<br>
      &nbsp;Return on Investment and Constantly Evaluate your<br>
      status. <span class="read-more">Read More</span></p>
    </div>
  </section>

  <div class="video-player" role="img" aria-label="Welcome video from the firm">
    <svg width="405" height="249" viewBox="0 0 405 249" style="position:absolute;left:0;top:0">
      <g fill="#9a9a9a">
        <circle cx="202" cy="106" r="2.2"/><circle cx="207" cy="109" r="2"/><circle cx="208" cy="115" r="1.8" fill-opacity=".8"/>
        <circle cx="203" cy="119" r="1.8" fill-opacity=".7"/><circle cx="197" cy="117" r="1.8" fill-opacity=".6"/>
        <circle cx="196" cy="111" r="2" fill-opacity=".9"/>
      </g>
    </svg>
    <div class="video-bar">
      <svg width="405" height="15" viewBox="0 0 405 15" style="position:absolute;left:0;top:0">
        <rect x="12" y="4" width="2" height="7" fill="#ccc"/><rect x="16" y="4" width="2" height="7" fill="#ccc"/>
        <polygon points="38,6 41,6 44,3 44,12 41,9 38,9" fill="#ccc"/>
        <circle cx="358" cy="7.5" r="2.5" fill="#ccc"/>
        <circle cx="376" cy="7.5" r="3.5" fill="none" stroke="#ccc" stroke-width="1.5"/>
        <rect x="390" y="3" width="9" height="9" fill="none" stroke="#ccc" stroke-width="1.2"/>
      </svg>
      <span class="video-time">0:00 / 0:16</span>
    </div>
  </div>

  <section class="intro">
    <h2>What is The New</h2>
    <p>Sample text - Far too often businesses seperate these two issues. Busi-<br>
    nesses that create a website as a stand alone enterprise seldom get<br>
    much of a Return on Investment. You may need to update your current<br>
    business plan. Your online platform will create new ways to reach your<br>
    current customer base as well as help you to find new customers. It will<br>
    allow you to Measure Results, calculate Return on Investment and Con-<br>
    stantly Evaluate your status.</p>
  </section>

  <footer>
    <div class="footer-links">
      <span>Copyright</span><span>Privacy Policy</span><span>Cookie policy</span><span>Sitemap</span>
      <span>Contact</span><span>Profile</span><span>Print</span><span>Email</span>
    </div>
    <div class="footer-band">2013 Dalton Tremayne, Inc. All rights reserved.</div>
  </footer>
</div>
</body>
</html>
```